Vex

I have the logo for the back already. Need the front to match.
Need a VEX logo which I can provide or you can download one - VEX Realty in canada... Back of the card will be my logo and name. Front will have the info...
I would like a black background. Match colors on front to the back..
Details on Card

Target Market(s)

Realestate clients.. Keep it classy like the logo

Contact Information for Business Card

Moren Tadwick office - 5817730264 cell - 5819063147 email - Moren@MorenTadwick.Com. website - MorenTadwick.Com Facebook - MTadwRealty Instagram - Moren_Qpl_Realtor Address - 418 - 23 St NE | K5P2M8

Colors
3176b5
33a6d7
85cae6

Requirements
Must have
• same color scheme as the logo
logo will be on the back
Black Background
Horizontal card
The one side of the card should be clean. like I stated, just my logo " Moren Tadwick " and nothing else

```html
<!DOCTYPE html>
<html lang="en">
<head>
<meta charset="utf-8">
<title>Moren Tadwick – Business Card</title>
<link rel="stylesheet" href="https://fonts.googleapis.com/css2?family=Cinzel:wght@500&family=Poppins:wght@400&display=swap">
<style>
  :root {
    --canvas: #2a2a2b;
    --card-dark: #1c1c1d;
    --card-light: #ffffff;
    --brand-blue: #1b76bd;
    --ink: #1a1a1a;
    --band-text: #9a9a9a;
    --rule: #333333;
  }
  * { margin: 0; padding: 0; box-sizing: border-box; }
  html, body {
    width: 1200px; height: 895px; overflow: hidden;
    background: var(--canvas);
  }
  .stage { position: relative; width: 1200px; height: 895px; }

  .card {
    position: absolute;
    width: 600px; height: 343px;
    box-shadow: 0 14px 30px rgba(0,0,0,.45);
  }

  /* Back side: name only */
  .card-back {
    left: 150px; top: 70px;
    background: var(--card-dark);
    display: flex; align-items: center; justify-content: center;
  }
  .wordmark {
    font-family: "Cinzel", serif;
    font-weight: 500;
    font-size: 44px;
    letter-spacing: 2px;
    color: var(--brand-blue);
  }

  /* Front side: details */
  .card-front {
    left: 450px; top: 482px;
    background: var(--card-light);
    overflow: hidden;
  }
  .identity {
    position: absolute; left: 48px; top: 148px;
  }
  .identity-name {
    font-family: "Cinzel", serif;
    font-weight: 500;
    font-size: 29px;
    color: var(--brand-blue);
    line-height: 1.1;
  }
  .identity-title {
    font-family: "Poppins", sans-serif;
    font-size: 19px;
    color: var(--ink);
    margin-top: 4px;
    padding-left: 34px;
  }
  .divider {
    position: absolute; left: 318px; top: 62px;
    width: 1px; height: 190px; background: var(--rule);
  }
  .contact-list {
    position: absolute; left: 340px; top: 62px;
    list-style: none;
  }
  .contact-item {
    display: flex; align-items: center; gap: 10px;
    height: 31px;
    font-family: "Poppins", sans-serif;
    font-size: 13.5px;
    color: var(--ink);
  }
  .contact-icon { width: 15px; height: 15px; flex: none; }
  .contact-icon svg { display: block; width: 15px; height: 15px; }
  .social-dot {
    width: 13px; height: 13px; border-radius: 50%;
    background: var(--brand-blue); flex: none; margin: 0 1px;
  }
  .address-band {
    position: absolute; left: 0; bottom: 0;
    width: 100%; height: 46px;
    background: var(--card-dark);
    display: flex; align-items: center; justify-content: center;
    font-family: "Poppins", sans-serif;
    font-size: 14px; letter-spacing: .5px;
    color: var(--band-text);
    padding-left: 200px;
  }
</style>
</head>
<body>
<main class="stage">
  <section class="card card-back" aria-label="Card back">
    <div class="wordmark">MOREN TADWICK</div>
  </section>

  <section class="card card-front" aria-label="Card front">
    <div class="identity">
      <div class="identity-name">MOREN TADWICK</div>
      <div class="identity-title">Founder &amp; CEO</div>
    </div>

    <div class="divider"></div>

    <ul class="contact-list">
      <li class="contact-item">
        <span class="contact-icon"><svg viewBox="0 0 16 16"><path fill="#1b76bd" d="M1 5c0-2 3-3 7-3s7 1 7 3v1h-3V5H4v1H1zM4 7h8l2 6H2z"/><circle cx="8" cy="10" r="1.6" fill="#fff"/></svg></span>
        5817730264
      </li>
      <li class="contact-item">
        <span class="contact-icon"><svg viewBox="0 0 16 16"><rect x="4" y="1" width="8" height="14" rx="1.5" fill="none" stroke="#1b76bd" stroke-width="1.6"/><circle cx="8" cy="12.5" r=".9" fill="#1b76bd"/></svg></span>
        5819063147
      </li>
      <li class="contact-item">
        <span class="contact-icon"><svg viewBox="0 0 16 16"><rect x="1" y="3" width="14" height="10" fill="#1b76bd"/><path d="M1 3l7 6 7-6" fill="none" stroke="#fff" stroke-width="1.2"/></svg></span>
        Moren@MorenTadwick.Com
      </li>
      <li class="contact-item">
        <span class="contact-icon"><svg viewBox="0 0 16 16" fill="none" stroke="#1b76bd" stroke-width="1.2"><circle cx="8" cy="8" r="6.5"/><ellipse cx="8" cy="8" rx="3" ry="6.5"/><path d="M1.5 8h13M2.5 5h11M2.5 11h11"/></svg></span>
        www.MorenTadwick.Com
      </li>
      <li class="contact-item">
        <span class="social-dot"></span>
        MTadwRealty
      </li>
      <li class="contact-item">
        <span class="social-dot"></span>
        Moren_Qpl_Realtor
      </li>
    </ul>

    <div class="address-band">418 - 23 St NE | K5P2M8</div>
  </section>
</main>
</body>
</html>
```